Pixel Harbor commercial brochure

We need a brochure that presents our services for commercial use. Without going into the details of our offers, that the prospect understands our added value and our expertise for the creation of a showcase site, e-commerce site and personalized, tailor-made application.

Please respect the graphic charter

Target Market(s)

Small and medium enterprises

Colors
F0912C
F2A743
F7CA91
FBE8D2
FDF5EE

Requirements
Must have
• a good presentation of our offers on several different pages
Nice to have
• little text but a lot of clarity and precision in the information
Should not have
• too much information, heavy design

```html
<!DOCTYPE html>
<html lang="fr">
<head>
<meta charset="utf-8">
<title>Pixel Harbor — brochure commerciale</title>
<link href="https://fonts.googleapis.com/css2?family=Bebas+Neue&family=Poppins:wght@400;500;600;700;800&display=swap" rel="stylesheet">
<style>
  :root{
    --orange:#f2480c;
    --orange-deep:#d93d06;
    --ink:#1c1c1c;
    --ink-soft:#2a2a2a;
    --text:#333;
    --paper:#ffffff;
    --backdrop:#a2a2a2;
    --line:#555;
  }
  *{box-sizing:border-box;margin:0;padding:0}
  html,body{width:899px;height:1200px;overflow:hidden}
  body{background:var(--backdrop);font-family:"Poppins",sans-serif;color:var(--text);position:relative}
  .page{position:absolute;width:367px;height:475px;background:var(--paper);overflow:hidden}
  .page--cover{left:68px;top:102px}
  .page--back{left:464px;top:102px}
  .page--inner-left{left:68px;top:624px}
  .page--inner-right{left:464px;top:624px}
  .abs{position:absolute}
  .accent{color:var(--orange)}
  .photo{position:absolute;background:linear-gradient(140deg,#2f3b4a,#7d8a99 60%,#c9ced4)}
  .photo--warm{background:linear-gradient(140deg,#3a3530,#8f8478 55%,#d8d2ca)}
  .photo--light{background:linear-gradient(150deg,#cfd6dc,#9aa6b2 55%,#4a5562)}
  .h-title{font-weight:800;color:var(--ink);text-transform:uppercase;line-height:1}
  .body-copy{font-size:4.6px;line-height:1.3;color:var(--text)}
  .body-copy p+p{margin-top:3px}

  /* cover */
  .brand{display:flex;align-items:center;gap:6px}
  .brand__mark{width:20px;height:20px;background:var(--orange)}
  .brand__name{font-size:13px;font-weight:600;color:var(--ink)}
  .cover__pattern{left:190px;top:0;width:177px;height:475px;
    background:linear-gradient(165deg,var(--orange) 0%,#f36a2c 35%,var(--ink) 55%,var(--orange) 80%,var(--ink) 100%);
    clip-path:polygon(45% 0,100% 0,100% 100%,62% 100%,10% 72%,28% 50%,0 28%)}
  .cover__photo{left:158px;top:132px;width:209px;height:270px;
    clip-path:polygon(0 22%,50% 0,100% 0,100% 100%,50% 100%,0 78%)}
  .cover__headline{left:24px;top:282px;font-family:"Bebas Neue",sans-serif;color:var(--orange);font-size:52px;line-height:44px}
  .cover__sub{left:25px;top:378px;font-size:15.5px;font-weight:800;color:var(--ink);line-height:17px}
  .cover__url{left:25px;top:441px;font-size:12px;letter-spacing:1.6px;color:var(--ink)}
  .cover__url b{color:var(--orange);font-weight:600}

  /* back page */
  .quality-card{position:absolute;top:53px;width:150px;height:94px}
  .quality-card .photo{left:2px;top:0;width:66px;height:92px;border:1px solid var(--ink)}
  .quality-card .corner{position:absolute;left:0;top:-2px;width:20px;height:3px;background:var(--orange)}
  .quality-card h4{position:absolute;left:72px;top:0;font-size:4.8px;font-weight:700;color:var(--orange)}
  .quality-card .body-copy{position:absolute;left:72px;top:7px;width:80px;font-size:4.4px}
  .graphics-panel{left:25px;top:154px;width:315px;height:89px;background:var(--ink);color:#fff;padding:6px 7px}
  .graphics-panel__title{font-size:12px;font-weight:800;color:var(--orange)}
  .graphics-panel__title span{font-size:7px;color:#fff}
  .graphics-panel__lead{font-size:4.6px;margin-top:2px}
  .graphics-panel__cols{display:flex;margin-top:6px}
  .graphics-panel__col{flex:1;text-align:center;font-size:4.6px;font-weight:600;line-height:1.3;padding:0 5px;border-right:1px solid #555}
  .graphics-panel__col:last-child{border:none}
  .graphics-panel__col svg{display:block;margin:0 auto 4px}
  .training__title{left:25px;top:252px;font-size:12px;line-height:12.5px}
  .training__copy{left:25px;top:281px;width:150px}
  .training__photo{left:193px;top:253px;width:148px;height:118px;border:1px solid var(--ink)}
  .training__corner{left:193px;top:251px;width:34px;height:3px;background:var(--orange)}
  .contact-band{left:0;top:389px;width:367px;height:86px;background:var(--orange);color:#fff}
  .contact-band .brand{position:absolute;left:25px;top:36px}
  .contact-band .brand__mark{background:#fff;width:14px;height:14px}
  .contact-band .brand__name{color:#fff;font-size:8px}
  .contact__head{position:absolute;left:91px;top:13px;width:256px;display:flex;align-items:center;gap:5px;font-size:9.5px;font-weight:700}
  .contact__head i{flex:1;height:1px;background:#fff;opacity:.8}
  .contact__grid{position:absolute;left:91px;top:31px;width:260px;font-size:6.8px;font-weight:500;display:grid;grid-template-columns:110px 150px;row-gap:3px}
  .contact__grid div{display:flex;align-items:center;gap:3px;white-space:nowrap}
  .contact__follow{position:absolute;left:94px;top:60px;font-size:6px;font-weight:600;display:flex;align-items:center;gap:3px}
  .contact__follow i{width:6px;height:6px;border-radius:50%;background:#fff;display:inline-block}

  /* inner left */
  .expertise__title{left:25px;top:29px;font-size:14.5px;line-height:14.5px}
  .expertise__intro{left:25px;top:62px;width:160px}
  .expertise__photo{left:212px;top:25px;width:131px;height:110px;border:1px solid var(--ink)}
  .expertise__accent{left:208px;top:100px;width:10px;height:40px;background:var(--orange)}
  .skills__title{left:25px;top:109px;font-size:12px}
  .skills__lead{left:25px;top:125px;width:180px}
  .tiles{left:25px;top:143px;width:318px;display:flex;gap:3px}
  .tile{flex:1;height:66px;position:relative;border:1px solid var(--ink)}
  .tile .photo{inset:0}
  .tile span{position:absolute;left:0;right:0;bottom:0;height:17px;background:var(--orange);color:#fff;font-size:5px;font-weight:700;display:flex;align-items:center;justify-content:center;text-align:center;line-height:1.1}
  .offer{position:absolute;top:222px;width:152px}
  .offer h3{font-size:7.8px;font-weight:700;color:var(--ink);margin-bottom:3px;white-space:nowrap}
  .offer h3 span{color:var(--orange)}
  .tools{left:26px;top:334px;width:317px;height:92px;background:var(--ink);color:#fff;padding:9px 10px}
  .tools h2{font-size:11px;font-weight:800;margin-bottom:5px}
  .tools .body-copy{color:#eee}
  .folio{position:absolute;left:25px;top:442px;width:318px;display:flex;align-items:center;gap:2px;font-size:7px;color:var(--ink)}
  .folio b{color:var(--orange);font-weight:600}
  .folio i{flex:1;height:1px;background:var(--ink)}
  .folio em{font-style:normal;width:10px;height:10px;border-radius:50%;background:var(--ink);color:#fff;font-size:5.5px;font-weight:700;display:flex;align-items:center;justify-content:center;border:1px solid var(--orange)}

  /* inner right */
  .services-bar{left:0;top:0;width:367px;height:63px;background:linear-gradient(180deg,#2b2b2b,var(--ink))}
  .services-bar h2{position:absolute;left:25px;top:20px;font-size:15px;font-weight:800;color:var(--orange)}
  .services-bar ul{position:absolute;left:25px;top:43px;list-style:none;display:flex;gap:10px;font-size:9.2px;font-weight:500;color:#fff}
  .services-bar li{display:flex;align-items:center;gap:2px}
  .services-bar li::before{content:"";width:5px;height:5px;border-radius:50%;background:var(--orange)}
  .app__title{left:25px;top:70px;font-size:12.5px}
  .app__copy{left:25px;top:87px;width:318px;font-size:4.5px}
  .app__copy strong{color:var(--ink)}
  .feature{position:absolute;width:150px;display:flex;gap:5px}
  .feature__icon{flex:none;width:26px;height:27px;background:var(--orange);display:flex;align-items:center;justify-content:center}
  .feature h4{font-size:6px;font-weight:700;color:var(--orange)}
  .feature p{font-size:4.5px;line-height:1.3}
  .commit__title{left:25px;top:257px;font-size:12.5px}
  .commit__copy{left:25px;top:274px;width:310px}
  .solutions{left:26px;top:296px;width:316px;height:132px;background:var(--ink);color:#fff;display:flex;padding-top:18px}
  .solutions__pill{left:63px;top:290px;width:241px;height:19px;background:var(--orange);border-radius:8px;color:#fff;font-size:11px;font-weight:700;display:flex;align-items:center;justify-content:center}
  .solution{flex:1;padding:0 4px;border-right:1px solid #555;text-align:center}
  .solution:last-child{border:none}
  .solution h3{font-size:9px;font-weight:800;color:var(--orange);margin-bottom:2px}
  .solution p{font-size:4.3px;line-height:1.25}
  .solution ul{text-align:left;list-style:none;margin-top:5px;font-size:4.3px;line-height:1.3}
  .solution li{padding-left:5px;position:relative}
  .solution li::before{content:"";position:absolute;left:0;top:1.4px;width:3px;height:3px;border-radius:50%;background:var(--orange)}
</style>
</head>
<body>

<!-- Cover -->
<section class="page page--cover">
  <div class="brand abs" style="left:25px;top:52px"><span class="brand__mark"></span><span class="brand__name">Pixel Harbor</span></div>
  <div class="cover__pattern abs" role="img" aria-label="Motif de triangles orange et noirs"></div>
  <div class="cover__photo photo" role="img" aria-label="Photo d'une équipe travaillant autour d'un ordinateur portable"></div>
  <h1 class="cover__headline abs">AGENCE<br>DIGITALE</h1>
  <p class="cover__sub abs">SPÉCIALISTE DU<br>WEB ET DES<br>APPLICATIONS MOBILES</p>
  <p class="cover__url abs">www.<b>pixelharbor</b>.studio</p>
</section>

<!-- Back page -->
<section class="page page--back">
  <h2 class="h-title abs" style="left:25px;top:23px;font-size:12.5px">UN CONTENU WEB <span class="accent">DE QUALITÉ</span></h2>
  <p class="body-copy abs" style="left:25px;top:40px">Nos rédacteurs développent avec vous une stratégie éditoriale pour un contenu garantissant visibilité et attractivité.</p>

  <article class="quality-card" style="left:25px">
    <span class="corner"></span>
    <div class="photo photo--warm" role="img" aria-label="Photo d'une équipe en réunion de travail"></div>
    <h4>LES FONDEMENTS DU WEB</h4>
    <p class="body-copy">Parce qu'une idée n'existe pas sans mots pour la dire, votre contenu est au cœur de toute stratégie digitale efficace. Quel que soit votre viatique de communication, la qualité de votre contenu est un élément essentiel, tant du point de vue de la crédibilité de votre image de marque que de celui de votre retour sur investissement (ROI).</p>
  </article>
  <article class="quality-card" style="left:191px">
    <span class="corner"></span>
    <div class="photo photo--light" role="img" aria-label="Photo d'un rédacteur travaillant sur ordinateur"></div>
    <h4>STRATÉGIE DIGITALE &amp; SEO</h4>
    <p class="body-copy">La visibilité de votre site est le résultat d'une stratégie digitale pertinente, d'un contenu et de liens de qualité (SEO-friendly) et d'une structure rédactionnelle appropriée. Nos rédacteurs web créent, reformulent et structurent vos contenus et messages afin d'obtenir un référencement naturel optimal sur les moteurs de recherche.</p>
  </article>

  <div class="graphics-panel abs">
    <p class="graphics-panel__title">GRAPHISME: <span>VOTRE IDENTITÉ VISUELLE, VOTRE UNIVERS</span></p>
    <p class="graphics-panel__lead">Vous cherchez à vous différencier et développer votre image de marque ?</p>
    <div class="graphics-panel__cols">
      <div class="graphics-panel__col">
        <svg width="12" height="12" viewBox="0 0 12 12"><circle cx="6" cy="6" r="4" fill="none" stroke="#f2480c" stroke-width="1.6"/><circle cx="6" cy="6" r="1.4" fill="#f2480c"/></svg>
        Vector of your brand identity, the logo in all variations, synthesizes your visual universe.
      </div>
      <div class="graphics-panel__col">
        <svg width="12" height="12" viewBox="0 0 12 12"><path d="M2 10 L10 2" stroke="#f2480c" stroke-width="2.2" stroke-linecap="round"/></svg>
        From design to layout, it gives visual consistency to your company's brand image.
      </div>
      <div class="graphics-panel__col">
        <svg width="12" height="12" viewBox="0 0 12 12"><ellipse cx="6" cy="6" rx="5" ry="3.2" fill="none" stroke="#f2480c" stroke-width="1.4"/><circle cx="6" cy="6" r="1.5" fill="#f2480c"/></svg>
        Pillar of your creative strategy, from color codes to the choice of typography and the digital and print design of your communication media.
      </div>
    </div>
  </div>

  <h2 class="h-title training__title abs">VOTRE FORMATION<br><span class="accent">PRISE EN CHARGE</span></h2>
  <div class="body-copy training__copy abs">
    <p>Pour maîtriser les outils que notre agence met en place pour votre entreprise et pour en exploiter tout le potentiel, nous vous proposons différentes formations en tant qu'organisme de formation certifié Qualiform.</p>
    <p>Pour rappel, ce dispositif vous permet de suivre une formation dispensée par nos soins en utilisant les budgets formations de votre entreprise.</p>
    <p>En effet, votre entreprise paie chaque année la contribution unique à la formation et à l'alternance. Cette contribution vous donne le droit à un budget formation annuel en fonction de votre organisme paritaire collecteur agréé (OPCF), du votre masse salariale, et de votre branche d'activité professionnelle.</p>
  </div>
  <span class="training__corner abs"></span>
  <div class="training__photo photo photo--light" role="img" aria-label="Photo d'une salle de formation avec participants levant la main"></div>

  <footer class="contact-band abs">
    <div class="brand"><span class="brand__mark"></span><span class="brand__name">Pixel Harbor</span></div>
    <p class="contact__head">CONTACT US <i></i></p>
    <div class="contact__grid">
      <div><svg width="7" height="7" viewBox="0 0 10 10"><circle cx="5" cy="5" r="5" fill="#fff"/><path d="M3 2.5 Q3 7 7.5 7.3 L7.5 6 L6.2 5.6 L5.6 6.2 Q4 5.4 3.8 4.4 L4.4 3.8 L4 2.5Z" fill="#f2480c"/></svg>04 00 12 34 56</div>
      <div><svg width="6" height="8" viewBox="0 0 6 8"><path d="M3 8 L0.6 4 A2.8 2.8 0 1 1 5.4 4Z" fill="#fff"/><circle cx="3" cy="2.8" r="1" fill="#f2480c"/></svg>18 rue des Lilas 13006 Marseille</div>
      <div><svg width="7" height="7" viewBox="0 0 10 10"><circle cx="5" cy="5" r="4.3" fill="none" stroke="#fff" stroke-width="1.2"/><path d="M1 5H9M5 1V9" stroke="#fff" stroke-width="1"/></svg>www.pixelharbor.studio</div>
      <div><svg width="8" height="6" viewBox="0 0 8 6"><rect width="8" height="6" fill="#fff"/><path d="M0 0 L4 3.5 L8 0" fill="none" stroke="#f2480c" stroke-width="0.8"/></svg>hello@pixelharbor.studio</div>
    </div>
    <p class="contact__follow">Follow us on <i></i><i></i></p>
  </footer>
</section>

<!-- Inner left page -->
<section class="page page--inner-left">
  <h2 class="h-title expertise__title abs">L'EXPERTISE WEB À<br><span class="accent">VOTRE SERVICE</span></h2>
  <p class="body-copy expertise__intro abs">Notre agence web propose une offre de services (développement de sites et d'applications mobiles, design, gestion de projet personnalisée et référencement de votre site web, conseil en communication et en marketing digital...) et de fonctionnalités adaptés aux objectifs professionnels de nos clients.</p>
  <span class="expertise__accent abs"></span>
  <div class="expertise__photo photo photo--light" role="img" aria-label="Photo d'une collaboratrice souriante devant son ordinateur"></div>
  <h2 class="h-title skills__title abs">NOTRE <span class="accent">EXPERTISE</span></h2>
  <p class="body-copy skills__lead abs">Réactivité, conseil et une proximité avec nos clients sont nos valeurs pour mener tous vos projets web de l'idée au succès !</p>
  <div class="tiles abs">
    <div class="tile"><div class="photo photo--warm" role="img" aria-label="Photo d'une équipe en réunion"></div><span>Community<br>management</span></div>
    <div class="tile"><div class="photo" style="background:linear-gradient(140deg,#e9e2d6,#f2480c 60%,#3b3b3b)" role="img" aria-label="Photo d'un nuancier et d'outils de design"></div><span>Graphisme</span></div>
    <div class="tile"><div class="photo" role="img" aria-label="Photo d'un écran affichant des applications mobiles"></div><span>Application<br>sur mesure</span></div>
    <div class="tile"><div class="photo photo--warm" role="img" aria-label="Photo d'un ordinateur portable sur un bureau en bois"></div><span>Un contenu web<br>de qualité</span></div>
    <div class="tile"><div class="photo photo--light" role="img" aria-label="Photo d'une formation en salle"></div><span>Formation</span></div>
  </div>

  <article class="offer" style="left:25px">
    <h3>Un site web <span>responsive de A à Z</span></h3>
    <div class="body-copy">
      <p>De la création de votre site en ligne (PressKit, ShopStack, Cmsly...) à son hébergement et son référencement gratuit sur Searchly, du choix d'un nom de domaine à la gestion et l'animation d'un blog en passant par la rédaction de contenus SEO pour vos pages et le lancement d'une campagne de marketing digital pour booster votre présence sur internet, notre offre est adaptée à toute entreprise, toute activité et gamme de prix.</p>
      <p>Notre équipe d'experts est à vos côtés pour développer votre projet de A à Z, lui donner vie en créant une solution de qualité aux outils et logiciels performants.</p>
    </div>
  </article>
  <article class="offer" style="left:191px">
    <h3>Une application <span>mobile performante</span></h3>
    <div class="body-copy">
      <p>Spécialisée dans la création de solutions mobiles au design sur mesure, notre agence web a développé une offre d'applications mobiles compatibles OrbitOS et Droidix au prix compétitif. Pour chaque version de votre application, l'ajout de fonctionnalités (éditeur de mise à jour, recherche de performances et d'avis clients, charte graphique...) et l'UX design sont pensés par nos développeurs et graphistes à votre service.</p>
      <p>Être à la pointe du digital grâce à votre application dédiée et personnalisée, disposer d'une vitrine et d'un vecteur d'informations pour vos clients est désormais accessible !</p>
      <p>Contactez-nous pour en savoir plus sur notre offre d'applications mobiles !</p>
    </div>
  </article>

  <div class="tools abs">
    <h2>NOS <span class="accent">OUTILS</span></h2>
    <div class="body-copy">
      <p>Dans le processus de création de votre site web, de votre blog ou de votre application mobile, nos équipes de développement, nos experts en design et en communication font appel aux outils les plus innovants afin de finaliser une solution efficace pour votre projet web.</p>
      <p>Chacun de nos outils permet de disposer de fonctionnalités de choix, d'optimiser vos contenus en français gratuitement, de développer un graphisme à l'esthétique choisie ou un CMS efficace, tel que PressKit, ShopStack, Cmsly</p>
      <p>Découvrez nos outils innovants au service de votre projet en ligne</p>
    </div>
  </div>
  <p class="folio">www.<b>pixelharbor</b>.studio<i></i><em>1</em></p>
</section>

<!-- Inner right page -->
<section class="page page--inner-right">
  <header class="services-bar abs">
    <h2>SERVICES</h2>
    <ul><li>Mobile app</li><li>Website</li><li>SEO writing</li><li>Graphics</li><li>Training</li></ul>
  </header>
  <h2 class="h-title app__title abs">APPLICATION <span class="accent">SUR MESURE</span></h2>
  <div class="body-copy app__copy abs">
    <p>Pixel Harbor développe des applications sur mesure, compatibles sur toutes les interfaces mobiles et tablettes.</p>
    <p>Our web agency specializes in the creation of tailor-made applications, with functionalities and personalized UX Design according to your projects, your service offering and your communication objectives with your customers.</p>
    <p>After designing a graphic project and developing the functionalities of your mobile application, our experts will support you to test, validate and implement the interface of your tool, from A to Z.</p>
    <p><strong>Contact us to take the mobile application approach, a solution for the future!</strong></p>
  </div>

  <div class="feature" style="left:25px;top:137px">
    <span class="feature__icon"><svg width="12" height="14" viewBox="0 0 12 14"><path d="M3 6V4a3 3 0 0 1 6 0v2" fill="none" stroke="#fff" stroke-width="1.5"/><rect x="1" y="6" width="10" height="8" fill="#fff"/></svg></span>
    <div><h4>Sécurité et accessibilité</h4><p>Nos développeurs conçoivent des applications rapides, sécurisées et fiables pour vos clients et usagers.</p></div>
  </div>
  <div class="feature" style="left:190px;top:137px">
    <span class="feature__icon"><svg width="16" height="13" viewBox="0 0 16 13"><rect x="1" y="1" width="14" height="9" fill="none" stroke="#fff" stroke-width="1.3"/><path d="M6 12H10" stroke="#fff" stroke-width="1.3"/></svg></span>
    <div><h4>Compatibility</h4><p>Toutes nos applications sont compatibles sur les interfaces mobiles (téléphones, tablettes) et systèmes d'exploitation OrbitOS et Droidix.</p></div>
  </div>
  <div class="feature" style="left:25px;top:173px">
    <span class="feature__icon"><svg width="12" height="15" viewBox="0 0 12 15"><circle cx="6" cy="6" r="4.5" fill="none" stroke="#fff" stroke-width="1.3"/><rect x="4" y="11" width="4" height="3" fill="#fff"/></svg></span>
    <div><h4>Innovation</h4><p>Votre application OrbitPhone ou Droidix est développée sur mesure. L'interface logicielle et le design sont développés avec des outils performants.</p></div>
  </div>
  <div class="feature" style="left:190px;top:173px">
    <span class="feature__icon"><svg width="14" height="14" viewBox="0 0 14 14"><circle cx="5" cy="3" r="2" fill="#fff"/><path d="M2 13V7h6l3 6" fill="none" stroke="#fff" stroke-width="1.3"/></svg></span>
    <div><h4>Ergonomics</h4><p>Le design et l'interface de votre application mobile sont adaptés pour garantir une expérience utilisateur de qualité.</p></div>
  </div>
  <div class="feature" style="left:25px;top:210px">
    <span class="feature__icon"><svg width="14" height="14" viewBox="0 0 14 14"><circle cx="7" cy="7" r="4" fill="none" stroke="#fff" stroke-width="2.4" stroke-dasharray="2 1.5"/><circle cx="7" cy="7" r="1.5" fill="#fff"/></svg></span>
    <div><h4>Stratégie digitale</h4><p>Notre équipe définit avec vous une campagne de communication et de marketing digital, en amont de chaque étape de la création de votre application mobile.</p></div>
  </div>
  <div class="feature" style="left:190px;top:210px">
    <span class="feature__icon"><svg width="15" height="13" viewBox="0 0 15 13"><rect x="1" y="1" width="13" height="8" fill="none" stroke="#fff" stroke-width="1.3"/><circle cx="7.5" cy="5" r="2" fill="none" stroke="#fff"/><path d="M5 12H10" stroke="#fff" stroke-width="1.3"/></svg></span>
    <div><h4>Suivi et adaptabilité</h4><p>Nos experts vous conseillent pour l'utilisation, la modification et la vision de votre positionnement digital et technique.</p></div>
  </div>

  <h2 class="h-title commit__title abs">NOTRE <span class="accent">ENGAGEMENT</span></h2>
  <p class="body-copy commit__copy abs">Pixel Harbor crée un site à votre image, adapté à vos besoins et permettant à votre projet de se démarquer des autres. En fonction de vos objectifs, notre agence web vous accompagne de l'idée au succès!</p>

  <div class="solutions abs">
    <div class="solution">
      <h3>SITE VITRINE</h3>
      <p>Outil webmarketing de base, il vous permet une visibilité sur le web et constitue votre image de marque auprès de clients potentiels.</p>
      <ul><li>Design du thème modifiable sur mesure</li><li>Pages entièrement administrables</li><li>15 pages personnalisables incluses</li><li>Formulaire de contact personnalisé</li><li>Carrousel d'image dynamique en page d'accueil</li><li>Hébergement et nom de domaine</li></ul>
    </div>
    <div class="solution">
      <h3>SITE E-COMMERCE</h3>
      <p>Outil indispensable à votre activité en ligne, le site e-commerce est optimisé afin de vous permettre la vente de produits et services avec une visibilité maximale dans un environnement web sécurisé.</p>
      <ul><li>Création d'articles et de catégories illimités</li><li>Gestion de commandes avancées</li><li>Module de codes promotionnels</li><li>Outils d'analyse statistique</li><li>Hébergement et nom de domaine inclus</li></ul>
    </div>
    <div class="solution">
      <h3>SITE SUR MESURE</h3>
      <p>Sa seule limite? Votre imagination! Le site sur mesure est un outil développé pour un projet spécifique, selon vos attentes, avec une équipe de conception graphique et de développeurs attentifs à relever les défis les plus complexes</p>
      <ul><li>Création d'un design et un univers graphique dédié</li><li>Outils web et framework adaptés</li><li>Optimisation de CMS professionnels</li><li>Développement de fonctionnalités supplémentaires</li><li>Adaptabilité à vos besoins techniques</li><li>Devis personnalisé</li></ul>
    </div>
  </div>
  <p class="solutions__pill abs">Votre besoin votre solution web</p>
  <p class="folio">www.<b>pixelharbor</b>.studio<i></i><em>2</em></p>
</section>

</body>
</html>
```